Webdesign for silver path

"Der Sternenpfad" is a new info product that will be selled through the website maybe you will create for us.

Translated from german to english the project is named "the silver path". It´s an online video course that teaches people how to live a fulfilling, happy and healthy life.

Design paramaters
We want a serious design that embodies the real feeling of beeing happy and fulfilled. Visitors should even feel good/better when they see the website.
In color psychology some sort of calming deep green like a four-leaf clover is recommend.
Mainly the website will be the external sales page with a big video as the central attention.
We also need a member area for customers to watch our video course.

So mainly we need a eye-cathing, calming header, the content body with mainly video and just a few written words...and of course a footer for links like imprint, affiliate program etc.

What we not want:
- some kind of these exaggerated smiling photos
- that bathetic luck symbols like money or boats
Updates

Hi,

i posted a message to the design discussion. Thank you!

Industry/Entity Type

Affiliate

```html
<!DOCTYPE html>
<html lang="en">
<head>
<meta charset="utf-8">
<title>Der Sternenpfad – Video Description</title>
<link href="https://fonts.googleapis.com/css2?family=Cinzel:wght@400;700&family=Arimo:wght@400;700&family=Marcellus&display=swap" rel="stylesheet">
<style>
:root{
  --teal:#2aa3b5;
  --teal-light:#49b7c6;
  --teal-dark:#2b6b75;
  --paper:#e9e3de;
  --paper-light:#f1ede9;
  --ink:#222;
  --muted:#666;
  --accent:#2a95a8;
  --field:#f3f0ed;
  --field-line:#cfc8c2;
  --white:#fff;
}
*{margin:0;padding:0;box-sizing:border-box}
html,body{width:756px;height:1200px;overflow:hidden}
body{position:relative;background:var(--paper);font-family:Arimo,Arial,sans-serif;color:var(--ink)}
.abs{position:absolute}
.header-band{left:0;top:0;width:756px;height:142px;background:linear-gradient(180deg,var(--teal) 0%,var(--teal-light) 100%)}
.search{left:411px;top:17px;width:163px;height:17px;background:var(--white)}
.search svg{position:absolute;right:3px;top:2px}
.top-links{left:340px;top:39px;font-family:Cinzel,serif;font-size:7px;color:var(--white);letter-spacing:.5px;word-spacing:2px}
.top-links span{margin:0 6px}
.tab{top:0;width:22px;height:55px;background:var(--teal-light);opacity:.9}
.tab svg{position:absolute;left:4px;top:35px}
.page{left:119px;top:120px;width:519px;height:848px;background:var(--paper)}
.main-nav{left:119px;top:120px;width:519px;height:21px;background:var(--teal-dark);border-radius:4px 4px 0 0;display:flex;justify-content:space-between;padding:0 12px;align-items:center;font-family:Cinzel,serif;font-size:8px;color:var(--white)}
.post-title{left:203px;top:174px;font-family:Cinzel,serif;font-size:13px;font-weight:400;letter-spacing:.5px}
.meta{left:128px;width:48px;text-align:right;font-size:5.5px;line-height:7px;color:var(--ink)}
.meta b{display:block;font-size:6px}
.date{left:128px;top:206px;width:48px;text-align:right;font-family:Cinzel,serif;color:var(--accent);font-size:11px;line-height:12px}
.video-frame{left:183px;top:205px;width:448px;height:370px;background:#dcd6d1}
.video-bar{left:183px;top:205px;width:448px;height:38px;background:linear-gradient(180deg,#5b5b5b,#2e2e2e)}
.video-area{left:193px;top:243px;width:426px;height:320px;background:linear-gradient(135deg,#4d4f4d,#2f312f)}
.side-btn{left:571px;width:42px;height:43px;background:#1d1d1d;border-radius:5px;color:var(--white);font-size:8px;font-weight:700;text-align:center;padding-top:27px}
.side-btn svg{position:absolute;left:12px;top:6px}
.pause{left:201px;top:502px;width:60px;height:46px;background:#1d1d1d;border-radius:4px}
.controls{left:270px;top:510px;width:342px;height:30px;background:#1d1d1d;border-radius:4px}
.progress{left:280px;top:525px;width:208px;height:12px;border:1px solid #aaa}
.progress i{display:block;width:16px;height:100%;background:#888}
.time{left:266px;top:502px;background:var(--white);font-size:8px;padding:1px 3px;border-radius:2px}
.brand-mark{left:556px;top:521px;color:var(--white);font-size:12px;font-weight:700}
.sec-title{font-family:Cinzel,serif;color:var(--accent);font-size:13px;font-weight:400}
.comment{left:119px;width:380px;font-size:5px;line-height:6px;color:#555}
.comment .avatar{position:absolute;width:38px;height:38px;background:#bbb;border:2px solid var(--white)}
.comment .head{position:absolute;font-size:8px;color:var(--ink);font-weight:700}
.comment .head em{font-style:normal;font-weight:400;color:var(--muted);font-size:6px}
.comment .head a{color:var(--accent);font-weight:400;font-size:6px;text-decoration:none}
.comment p{position:absolute;width:290px}
.thumb{width:30px;height:30px;background:linear-gradient(135deg,#d9d9d9,#8a8a8a);border:2px solid var(--teal)}
.sim{left:508px;width:130px}
.sim .thumb{position:absolute;left:0;top:0}
.sim h4{position:absolute;left:44px;top:0;font-size:6px;color:var(--accent);font-weight:400}
.sim p{position:absolute;left:43px;top:8px;width:88px;font-size:4.5px;line-height:5.5px;color:#666}
.new-thumb{width:26px;height:40px;background:linear-gradient(160deg,#e8e8e8,#8e8e8e);border:2px solid var(--teal)}
.divider{height:1px;background:#cfc8c2}
.form-label{font-size:7px}
.field{background:var(--field);border:1px solid var(--field-line)}
.submit{left:249px;top:924px;width:54px;height:15px;background:#cdbfb2;font-family:Cinzel,serif;font-size:7px;text-align:center;line-height:15px;color:#333}
.footer{left:0;top:940px;width:756px;height:228px;background:linear-gradient(180deg,var(--teal),var(--teal-light))}
.foot-head{color:var(--white);font-family:Marcellus,serif;font-size:15px;font-weight:400}
.foot-text{font-size:5px;line-height:7px}
.social{top:1097px;width:26px;height:26px;border-radius:50%;background:var(--white);border:2px solid #1c6d7a;font-size:5px;text-align:center;line-height:22px;color:#1c6d7a;font-weight:700}
.login-label{left:464px;font-size:6px;color:var(--white)}
.login-field{left:501px;width:119px;height:15px;background:var(--white);border:1px solid #bcd}
.signin{left:566px;top:1079px;width:55px;height:16px;background:#8e9aa0;color:var(--white);font-size:6px;line-height:16px;padding-left:9px;border-radius:2px}
.create{left:505px;top:1136px;width:121px;height:16px;background:linear-gradient(#f1f4f6,#c9d3d8);border-radius:2px;font-size:7px;color:#333;text-align:center;line-height:16px}
.copyright{left:390px;top:1168px;font-size:5.5px;color:#555;line-height:7px}
</style>
</head>
<body>

<div class="abs header-band" role="img" aria-label="Calm teal header band with soft wave pattern"></div>
<div class="abs search"><svg width="12" height="12" viewBox="0 0 12 12"><circle cx="5" cy="5" r="3.5" fill="none" stroke="#bbb" stroke-width="1.5"/><line x1="7.5" y1="7.5" x2="11" y2="11" stroke="#bbb" stroke-width="1.5"/></svg></div>
<div class="abs top-links">MAPA DEL SITIO<span>|</span>CONTÁCTENOS<span>|</span>EVENTOS<span>|</span>INICIO</div>
<div class="abs tab" style="left:583px"><svg width="14" height="12" viewBox="0 0 14 12"><path d="M1 6 L7 1 L13 6 M3 5 V11 H11 V5" fill="#fff"/></svg></div>
<div class="abs tab" style="left:617px"><svg width="14" height="11" viewBox="0 0 14 11"><rect x="1" y="1" width="12" height="9" fill="none" stroke="#fff" stroke-width="1.5"/><path d="M1 1 L7 6 L13 1" fill="none" stroke="#fff" stroke-width="1.5"/></svg></div>

<div class="abs page"></div>
<nav class="abs main-nav"><span>HOME</span><span>COURSES</span><span>MEMBERS</span><span>ABOUT US</span><span>CONTACT US</span><span>WHY US</span></nav>

<h1 class="abs post-title">VIDEO DISCRIPTION.</h1>
<div class="abs date">24<br>August</div>
<div class="abs meta" style="top:254px"><span style="font-size:11px;line-height:12px;display:block">2</span>Comments</div>
<div class="abs meta" style="top:293px"><b>Features</b>Jonas</div>
<div class="abs meta" style="top:328px"><b>Categories:</b>Course, Yoga, Central, Meditation</div>
<div class="abs meta" style="top:370px"><b>Share on:</b>Friendwall<br>Chirper<br>Circleup</div>

<div class="abs video-frame"></div>
<div class="abs video-bar"></div>
<div class="abs video-area" role="img" aria-label="Video course preview still"></div>
<div class="abs side-btn" style="top:253px"><svg width="18" height="16" viewBox="0 0 18 16"><path d="M9 15 L2 8 A4 4 0 0 1 9 3 A4 4 0 0 1 16 8 Z" fill="#fff"/></svg>LIKE</div>
<div class="abs side-btn" style="top:303px"><svg width="18" height="16" viewBox="0 0 18 16"><path d="M3 13 L15 3 M9 3 H15 V9" fill="none" stroke="#fff" stroke-width="2"/></svg>SHARE</div>
<div class="abs side-btn" style="top:354px"><svg width="18" height="16" viewBox="0 0 18 16"><path d="M5 3 L1 8 L5 13 M13 3 L17 8 L13 13 M10 2 L8 14" fill="none" stroke="#fff" stroke-width="2"/></svg>EMBED</div>
<div class="abs pause"><svg width="60" height="46"><rect x="23" y="14" width="5" height="18" fill="#fff"/><rect x="32" y="14" width="5" height="18" fill="#fff"/></svg></div>
<div class="abs controls"></div>
<div class="abs progress"><i></i></div>
<div class="abs time">00:03</div>
<svg class="abs" style="left:496px;top:524px" width="50" height="14"><rect x="0" y="1" width="2" height="12" fill="#d4207b"/><rect x="4" y="1" width="2" height="12" fill="#d4207b"/><rect x="8" y="1" width="2" height="12" fill="#888"/><rect x="12" y="1" width="2" height="12" fill="#888"/><rect x="16" y="1" width="2" height="12" fill="#888"/><path d="M28 2 L32 6 M42 2 L38 6 M28 12 L32 8 M42 12 L38 8" stroke="#fff" stroke-width="2"/></svg>
<div class="abs brand-mark">fenlark</div>

<h2 class="abs sec-title" style="left:131px;top:591px">➔ 2 Comments</h2>
<div class="abs divider" style="left:119px;top:613px;width:380px"></div>
<div class="abs comment" style="top:614px;height:62px;background:var(--paper-light)">
  <div class="avatar" style="left:26px;top:12px" role="img" aria-label="Commenter avatar"></div>
  <div class="head" style="left:76px;top:12px">Jonas Lindqvist <em>| August 17, 2009 |</em> <a>Reply</a></div>
  <p style="left:76px;top:26px">Lorem ipsum dolor sit amet, consectetur adipiscing elit, sed do eiusmod tempor incididunt ut labore et dolore magna aliqua. Ut enim ad minim veniam, quis nostrud exercitation ullamco laboris nisi ut aliquip ex ea commodo consequat duis aute.</p>
</div>
<div class="abs comment" style="top:676px;height:78px">
  <div class="avatar" style="left:77px;top:13px" role="img" aria-label="Commenter avatar"></div>
  <div class="head" style="left:130px;top:13px">Jonas <em>| August 22, 2012 |</em> <a>Reply</a></div>
  <p style="left:130px;top:27px;width:245px">Lorem ipsum dolor sit amet, consectetur adipiscing elit, sed do eiusmod tempor incididunt ut labore et dolore magna aliqua. Ut enim ad minim veniam, quis nostrud exercitation ullamco laboris nisi ut aliquip ex ea commodo consequat duis aute.</p>
</div>
<div class="abs divider" style="left:119px;top:754px;width:380px"></div>

<h2 class="abs sec-title" style="left:508px;top:591px">Similar Videos</h2>
<div class="abs sim" style="top:620px"><div class="thumb" role="img" aria-label="Video thumbnail"></div><h4>video number 1</h4><p>Lorem ipsum ne pro nihil saperet, assentior eu vis summo elect, mel soluta feugait intellegam eu.</p></div>
<div class="abs sim" style="top:673px"><div class="thumb" role="img" aria-label="Video thumbnail"></div><h4>video number 1</h4><p>Lorem ipsum ne pro nihil saperet, assentior eu vis summo elect, mel soluta feugait intellegam eu.</p></div>
<div class="abs sim" style="top:726px"><div class="thumb" role="img" aria-label="Video thumbnail"></div><h4>video number 1</h4><p>Lorem ipsum ne pro nihil saperet, assentior eu vis summo elect, mel soluta feugait intellegam eu.</p></div>
<div class="abs sim" style="top:779px"><div class="thumb" role="img" aria-label="Video thumbnail"></div><h4>video number 1</h4><p>Lorem ipsum ne pro nihil saperet, assentior eu vis summo elect, mel soluta feugait intellegam eu.</p></div>
<h2 class="abs sec-title" style="left:510px;top:826px">New Videos</h2>
<div class="abs new-thumb" style="left:508px;top:851px" role="img" aria-label="Video thumbnail"></div>
<div class="abs new-thumb" style="left:539px;top:851px" role="img" aria-label="Video thumbnail"></div>
<div class="abs new-thumb" style="left:570px;top:851px" role="img" aria-label="Video thumbnail"></div>
<div class="abs new-thumb" style="left:602px;top:851px" role="img" aria-label="Video thumbnail"></div>
<div class="abs new-thumb" style="left:508px;top:899px" role="img" aria-label="Video thumbnail"></div>
<div class="abs new-thumb" style="left:539px;top:899px" role="img" aria-label="Video thumbnail"></div>
<div class="abs new-thumb" style="left:570px;top:899px" role="img" aria-label="Video thumbnail"></div>
<div class="abs new-thumb" style="left:602px;top:899px" role="img" aria-label="Video thumbnail"></div>

<h2 class="abs" style="left:130px;top:776px;font-family:Cinzel,serif;font-size:13px;font-weight:400">Your Comment:-</h2>
<div class="abs form-label" style="left:130px;top:812px">Number:</div>
<div class="abs field" style="left:130px;top:823px;width:172px;height:15px"></div>
<div class="abs form-label" style="left:130px;top:850px">E-mail:</div>
<div class="abs field" style="left:130px;top:861px;width:172px;height:15px"></div>
<div class="abs form-label" style="left:130px;top:888px">Web Site:</div>
<div class="abs field" style="left:130px;top:899px;width:172px;height:15px"></div>
<div class="abs form-label" style="left:314px;top:812px">Message:</div>
<div class="abs field" style="left:314px;top:823px;width:173px;height:116px"></div>
<div class="abs submit">Submit</div>

<div class="abs footer" role="img" aria-label="Teal footer band with soft wave pattern"></div>
<div class="abs page" style="top:940px;height:28px"></div>

<h3 class="abs foot-head" style="left:120px;top:985px">Chirper</h3>
<div class="abs foot-text" style="left:120px;top:1023px;width:118px;color:#000">
  <b>Design paramaters</b><br>We want a serious design that embodies the real feeling of beeing happy and fulfilled. Visitors should even feel good/better when they see the website.<br>In color psychology some sort of calming deep green like a four-leaf clover is recommend.<br>Mainly the website will be the external sales page with a big video as the central attention.
</div>
<div class="abs divider" style="left:120px;top:1089px;width:118px;background:#7cc"></div>
<div class="abs social" style="left:152px" aria-label="Chirper">CH</div>
<div class="abs social" style="left:182px" aria-label="Friendwall">FW</div>
<div class="abs social" style="left:211px" aria-label="Feed">RSS</div>

<h3 class="abs foot-head" style="left:283px;top:983px">Affiliate Program:-</h3>
<div class="abs foot-text" style="left:284px;top:1013px;width:118px;color:var(--white)">
  <b>Our Affiliate Program.</b><br>Design paramaters<br>We want a serious design that embodies the real feeling of beeing happy and fulfilled. Visitors should even feel good/better when they see the website.<br>In color psychology some sort of calming deep green like a four-leaf clover is recommend.<br>Mainly the website will be the external sales page with a big video as the central attention.<br>We also need a member area for customers to watch our video course.
</div>
<div class="abs divider" style="left:284px;top:1122px;width:118px;background:#7cc"></div>

<h3 class="abs foot-head" style="left:466px;top:983px;font-family:Arimo,sans-serif;font-size:17px">Members Login</h3>
<div class="abs login-label" style="top:1031px">Username</div>
<div class="abs login-field" style="top:1025px"></div>
<div class="abs login-label" style="top:1055px">Password</div>
<div class="abs login-field" style="top:1049px"></div>
<div class="abs signin">Sign-in <span style="margin-left:12px">▸</span></div>
<div class="abs" style="left:543px;top:1106px;color:var(--white);font-size:16px">OR</div>
<div class="abs create">Create an account</div>

<div class="abs copyright">© 2012 Todos los derechos<br>Reservador.</div>

</body>
</html>
```